Business card design needed

I would like a one sided black business card with the information provided above. Refer to my website www.lobcrafttennis.com.au for an example of colors I have used for my site, would like to keep this consistent for my business cards also, I will upload my logo below.

I am a new small business that provides tennis customers with racquet re stringing, tennis strings and accessories.

Industry/Entity Type

Small Business

Contact Information for Business Card

Lob Craft Tennis

Dennis Morrow
Managing Director

lobcrafttennis@mailbay.com
www.lobcrafttennis.com.au
0412 695 203

Racquet Restringing/Tennis Strings/Accessories

Requirements
Must have
• Must have my logo and card must be black

```html
<!DOCTYPE html>
<html lang="en">
<head>
<meta charset="utf-8">
<title>Lob Craft Tennis – Business Card</title>
<link rel="stylesheet" href="https://fonts.googleapis.com/css2?family=Aldrich&display=swap">
<style>
  :root {
    --page-bg: #ffffff;
    --card-dark: #0f1011;
    --card-mid: #1c1e20;
    --card-light: #2b2e31;
    --lime: #b4d335;
    --sky: #5c8fd8;
    --white: #f4f4f4;
  }
  * { margin: 0; padding: 0; box-sizing: border-box; }
  html, body {
    width: 1200px;
    height: 1200px;
    overflow: hidden;
    background: var(--page-bg);
  }
  body {
    position: relative;
    font-family: "Aldrich", sans-serif;
  }
  .business-card {
    position: absolute;
    left: 160px;
    top: 342px;
    width: 880px;
    height: 515px;
    background:
      radial-gradient(ellipse 70% 80% at 80% 45%, var(--card-light) 0%, var(--card-mid) 45%, var(--card-dark) 100%);
    overflow: hidden;
  }
  .brand {
    position: absolute;
    left: 458px;
    top: 92px;
    width: 362px;
    text-align: center;
  }
  .brand-name {
    color: var(--lime);
    font-size: 36px;
    letter-spacing: 2px;
    text-transform: uppercase;
    white-space: nowrap;
    line-height: 1;
  }
  .brand-services {
    margin-top: 78px;
    color: var(--sky);
    font-size: 13px;
    white-space: nowrap;
    letter-spacing: 0.2px;
  }
  .brand-services .divider { margin: 0 6px; }
  .contact-block {
    position: absolute;
    left: 67px;
    top: 308px;
  }
  .person-name {
    color: var(--white);
    font-size: 34px;
    letter-spacing: 0.5px;
    text-transform: uppercase;
    line-height: 1;
    font-weight: 400;
  }
  .person-role {
    margin-top: 8px;
    color: var(--white);
    font-size: 20px;
    line-height: 1;
  }
  .contact-list {
    list-style: none;
    margin-top: 16px;
  }
  .contact-line {
    display: flex;
    align-items: center;
    gap: 6px;
    line-height: 26px;
    white-space: nowrap;
  }
  .contact-icon { width: 14px; height: 14px; flex: none; }
  .contact-phone { color: var(--sky); font-size: 21px; }
  .contact-phone .plus { color: var(--lime); font-size: 16px; margin-right: 2px; }
  .contact-email { color: var(--sky); font-size: 21px; }
  .contact-email .contact-icon { margin-right: 8px; }
  .contact-web { color: var(--lime); font-size: 21px; }
</style>
</head>
<body>
  <section class="business-card">
    <div class="brand">
      <div class="brand-name">Lob Craft Tennis</div>
      <div class="brand-services">
        Racquet Restringing<span class="divider">|</span>Tennis Strings<span class="divider">|</span>Accessories
      </div>
    </div>

    <div class="contact-block">
      <h1 class="person-name">Dennis Morrow</h1>
      <p class="person-role">Managing Director</p>
      <ul class="contact-list">
        <li class="contact-line contact-phone">
          <svg class="contact-icon" viewBox="0 0 16 16" aria-hidden="true">
            <path d="M3 2l3 0 1 4-2 1c1 2 2 3 4 4l1-2 4 1v3c-7 0-11-4-11-11z" fill="var(--lime)"/>
          </svg>
          <span><span class="plus">+</span>0412 695 203</span>
        </li>
        <li class="contact-line contact-email">
          <svg class="contact-icon" viewBox="0 0 16 16" aria-hidden="true">
            <rect x="1" y="4" width="14" height="9" fill="var(--lime)"/>
            <path d="M1 4l7 5 7-5" fill="none" stroke="var(--card-dark)" stroke-width="1.4"/>
          </svg>
          <span>lobcrafttennis@mailbay.com</span>
        </li>
        <li class="contact-line contact-web">www.lobcrafttennis.com.au</li>
      </ul>
    </div>
  </section>
</body>
</html>
```